Tactical Supply Company needing memorable business card design

Our tactical supply comapny is in need of a new business card design that will set us apart from the amateurs. We sell tactical gear ranging from backpacks and range bags to apparel and other gear. We are looking for a sharp design that incorporates our logo, website, and name. Our colors are white, red, and black, or any combination of the three, preferably red and black.
I have attached our logo with our name underneath but I have also edited that design with the logo incorporated next to the name (attached).

Target Market(s)

Law enforcement, military, tactical

Industry/Entity Type

Business

Contact Information for Business Card

Include www.fernhollowprovisions-demo.com

Colors
000000
ec1f27
ffffff

Requirements
Must have
• Our name, logo, and website. This is intended to be a memorable simple card, no name, address, email, or phone number info is necessary. Designs that do include this additional info will still be considered if they are absolutely spectacular.
Should not have
• A standard template design, I can create that in my own on Cardvellum. I am looking for a new, creative design that is completely unique to my company.

```html
<!DOCTYPE html>
<html lang="en">
<head>
<meta charset="utf-8">
<title>Fern Hollow Provisions — Business Card</title>
<link rel="stylesheet" href="https://fonts.googleapis.com/css2?family=Montserrat:wght@300;800&display=swap">
<style>
  :root {
    --ink: #000000;
    --ink-soft: #0b0b0b;
    --brand-red: #ec1f27;
    --paper: #ffffff;
    --paper-tint: #ededed;
    --backdrop: #ffffff;
    --faint-mark: #1c1c1c;
    --name-ink: #1d1d1d;
  }
  html, body {
    margin: 0;
    width: 1200px;
    height: 1000px;
    overflow: hidden;
    background: var(--backdrop);
  }
  .canvas {
    position: relative;
    width: 1200px;
    height: 1000px;
  }
  .card {
    position: absolute;
    left: 280px;
    top: 180px;
    width: 640px;
    height: 640px;
    border-radius: 44px;
    overflow: hidden;
    background: var(--ink-soft);
    box-shadow: 0 10px 30px rgba(0,0,0,0.18);
  }
  .card__top {
    position: absolute;
    left: 0; top: 0;
    width: 100%;
    height: 350px;
    background: linear-gradient(180deg, var(--paper-tint), #f6f6f6 60%, var(--paper-tint));
  }
  .brand {
    position: absolute;
    left: 0; right: 0;
    top: 125px;
    display: flex;
    align-items: center;
    justify-content: center;
    gap: 22px;
  }
  .brand__square {
    width: 58px;
    height: 58px;
    background: var(--brand-red);
    flex: none;
  }
  .brand__name {
    font-family: "Montserrat", sans-serif;
    font-weight: 800;
    font-size: 44px;
    line-height: 1.02;
    letter-spacing: 1px;
    color: var(--name-ink);
    text-transform: uppercase;
    margin: 0;
  }
  .tab {
    position: absolute;
    left: 50%;
    top: 300px;
    width: 200px;
    height: 100px;
    transform: translateX(-50%);
  }
  .website {
    position: absolute;
    left: 0; right: 0;
    top: 450px;
    margin: 0;
    text-align: center;
    font-family: "Montserrat", sans-serif;
    font-weight: 300;
    font-size: 22px;
    letter-spacing: 1.5px;
    color: var(--paper);
    text-transform: uppercase;
  }
  .faint-mark {
    position: absolute;
    left: 50%;
    top: 540px;
    width: 44px;
    height: 44px;
    transform: translateX(-50%);
    background: var(--faint-mark);
  }
</style>
</head>
<body>
<main class="canvas">
  <article class="card">
    <section class="card__top">
      <div class="brand">
        <span class="brand__square"></span>
        <h1 class="brand__name">Fern Hollow<br>Provisions</h1>
      </div>
    </section>

    <svg class="tab" viewBox="0 0 200 100" aria-hidden="true">
      <polygon points="45,0 155,0 200,50 170,90 30,90 0,50" fill="#ec1f27"/>
      <polygon points="0,50 200,50 170,90 30,90" fill="#c8161d"/>
      <rect x="82" y="27" width="36" height="36" rx="8" fill="#ffffff"/>
      <g fill="none" stroke="#ec1f27" stroke-width="2.2">
        <circle cx="100" cy="45" r="10"/>
        <ellipse cx="100" cy="45" rx="4.5" ry="10"/>
        <line x1="90" y1="45" x2="110" y2="45"/>
      </g>
    </svg>

    <p class="website">www.fernhollowprovisions-demo.com</p>
    <span class="faint-mark"></span>
  </article>
</main>
</body>
</html>
```